Banners for Affiliate Marketing on Tantra website

We are starting an affiliate marketing program on our website brightmeadowhub.com and need banner ads for our affiliates. We are looking for the following sizes

for sure: 728x90, 300x250, 160x600
possibly: 468x60, 250x250, 125x125

Banner ads should market a several of our products - online tantra store, various tantra workshops, tantra vacations. See our website for details on what we offer.

For example, EITHER we may need one banner ad each in different sizes for:

Women's Workshop
Tantra Vacations
Tantric Massage workshop
Golden Hearth workshop
Joy & Harmony Course
Selected products from our store, for example Gentle Touch for Partners DVD, or Wendel Bundle

OR maybe we just need one banner ad in all the sizes for
Workshops
Store
Vacations

All images on our site can be used, or use other stock images.

The winner of this project will continue to work with us on graphic design of future banners, and we are also looking for a logo design.

Target Market(s)

couples, singles, age group 28-65, with disposable income

Industry/Entity Type

Graphic Design

Requirements
Must have
• Modern, attractive design that matches the branding and coloring on our website.
Should not have
• no obvious nudity in any graphics

```html
<!DOCTYPE html>
<html lang="en">
<head>
<meta charset="utf-8">
<title>Bright Meadow Institute – Affiliate Banners</title>
<link href="https://fonts.googleapis.com/css2?family=Bebas+Neue&family=Cinzel:wght@400;500&display=swap" rel="stylesheet">
<style>
  :root {
    --stage: #111111;
    --banner-black: #050505;
    --ink-light: #f4f1ea;
    --gold-light: #fbe38a;
    --gold: #e0b43a;
    --gold-deep: #a8741a;
    --silver: #6b6b6b;
    --badge-ink: #2a1a05;
    --sea-light: #bfe8ec;
    --sea: #6cc6cf;
    --sand: #efe6d4;
    --portrait-light: #f2eee8;
    --portrait-warm: #d9b79b;
  }
  * { box-sizing: border-box; margin: 0; padding: 0; }
  html, body {
    width: 1200px; height: 812px; overflow: hidden;
    background: var(--stage);
  }
  .stage { position: relative; width: 1200px; height: 812px; }

  .banner {
    position: absolute; overflow: hidden;
    background: var(--banner-black);
    font-family: "Cinzel", Georgia, serif;
    color: var(--ink-light);
  }
  .banner__photo { position: absolute; }
  .banner__swoosh { position: absolute; inset: 0; width: 100%; height: 100%; }

  .photo--beach {
    background: linear-gradient(180deg, var(--sea-light) 0%, var(--sea) 38%, #a9d9d6 52%, var(--sand) 70%, #f6f1e6 100%);
  }
  .photo--portrait {
    background: linear-gradient(90deg, var(--portrait-light) 0%, var(--portrait-warm) 45%, #e8ddd2 60%, var(--portrait-warm) 80%, #bfa08a 100%);
  }

  .brand { display: flex; flex-direction: column; align-items: center; text-align: center; }
  .brand__dot {
    width: 14px; height: 14px; border-radius: 50%;
    background: var(--gold); margin-bottom: 8px;
  }
  .brand__name { font-weight: 400; line-height: 1.2; color: var(--ink-light); }

  .headline { text-align: center; font-weight: 400; line-height: 1.15; color: var(--ink-light); }
  .headline__rule {
    display: block; height: 1px; margin: 6px auto;
    background: linear-gradient(90deg, transparent, var(--silver), transparent);
  }

  .badge {
    position: absolute; border-radius: 50%;
    background: radial-gradient(circle at 35% 30%, var(--gold-light) 0%, var(--gold) 45%, var(--gold-deep) 100%);
    border: 3px solid var(--gold-light);
    box-shadow: 0 0 0 2px var(--gold-deep);
    display: flex; align-items: center; justify-content: center; text-align: center;
    font-family: "Bebas Neue", Impact, sans-serif;
    color: var(--badge-ink); line-height: 0.95;
  }

  /* 160x600 skyscraper */
  .skyscraper { left: 41px; top: 37px; width: 198px; height: 742px; }
  .skyscraper .banner__photo { left: 0; top: 300px; width: 198px; height: 442px; }
  .skyscraper .brand { position: absolute; top: 30px; left: 0; width: 100%; }
  .skyscraper .brand__dot { width: 26px; height: 26px; margin-bottom: 14px; }
  .skyscraper .brand__name { font-size: 18px; }
  .skyscraper .headline { position: absolute; top: 152px; left: 0; width: 100%; font-size: 29px; }
  .skyscraper .headline__rule { width: 120px; margin: 8px auto; }
  .skyscraper .badge { left: 32px; top: 334px; width: 128px; height: 128px; font-size: 38px; }

  /* 728x90 leaderboard */
  .leaderboard { left: 261px; top: 239px; width: 902px; height: 111px; }
  .leaderboard .banner__photo { left: 560px; top: 0; width: 342px; height: 111px; }
  .leaderboard .brand { position: absolute; left: 16px; top: 14px; width: 130px; }
  .leaderboard .brand__dot { width: 20px; height: 20px; margin-bottom: 8px; }
  .leaderboard .brand__name { font-size: 15px; }
  .leaderboard .headline { position: absolute; left: 160px; top: 18px; width: 330px; font-size: 30px; }
  .leaderboard .headline__rule { width: 240px; margin: 4px auto; }
  .leaderboard .badge { left: 508px; top: 10px; width: 92px; height: 92px; font-size: 27px; }

  /* 300x250 rectangle */
  .rectangle { left: 261px; top: 371px; width: 372px; height: 309px; }
  .rectangle .banner__photo { left: 0; top: 124px; width: 372px; height: 185px; }
  .rectangle .brand { position: absolute; left: 76px; top: 12px; flex-direction: row; gap: 14px; }
  .rectangle .brand__dot { width: 24px; height: 24px; margin: 0; }
  .rectangle .brand__name { font-size: 15px; }
  .rectangle .headline { position: absolute; left: 0; top: 56px; width: 100%; font-size: 27px; }
  .rectangle .headline__rule { width: 250px; margin: 2px auto; }
  .rectangle .badge { left: 206px; top: 180px; width: 112px; height: 112px; font-size: 35px; }
</style>
</head>
<body>
<main class="stage">

  <section class="banner skyscraper" aria-label="160 by 600 banner">
    <div class="banner__photo photo--beach" role="img" aria-label="Photo of a couple sitting together on a tropical beach"></div>
    <svg class="banner__swoosh" viewBox="0 0 198 742" preserveAspectRatio="none" aria-hidden="true">
      <defs>
        <linearGradient id="skyGold" x1="0" y1="0" x2="0" y2="1">
          <stop offset="0" stop-color="#fbe38a"/><stop offset="0.5" stop-color="#e0b43a"/><stop offset="1" stop-color="#a8741a"/>
        </linearGradient>
      </defs>
      <path d="M0 0 H198 V330 C170 400 90 500 0 560 Z" fill="#050505"/>
      <path d="M198 340 C172 420 96 510 0 572 V560 C90 500 168 410 198 330 Z" fill="url(#skyGold)"/>
      <path d="M198 350 C176 430 100 520 0 585 V572 C96 510 172 420 198 340 Z" fill="#4a4a4a"/>
    </svg>
    <div class="brand">
      <span class="brand__dot"></span>
      <p class="brand__name">Bright Meadow<br>Institute</p>
    </div>
    <h2 class="headline">
      Tantra<br>Workshops
      <span class="headline__rule"></span>
      Store
      <span class="headline__rule"></span>
      Vacations
    </h2>
    <a class="badge">LEARN<br>MORE</a>
  </section>

  <section class="banner leaderboard" aria-label="728 by 90 banner">
    <div class="banner__photo photo--portrait" role="img" aria-label="Photo of a smiling mature couple lying face to face"></div>
    <svg class="banner__swoosh" viewBox="0 0 902 111" preserveAspectRatio="none" aria-hidden="true">
      <defs>
        <linearGradient id="leadGold" x1="0" y1="0" x2="1" y2="1">
          <stop offset="0" stop-color="#fbe38a"/><stop offset="1" stop-color="#a8741a"/>
        </linearGradient>
      </defs>
      <path d="M0 0 H560 C556 40 560 80 590 111 H0 Z" fill="#050505"/>
      <path d="M560 0 H578 C570 40 578 80 612 111 H590 C560 80 556 40 560 0 Z" fill="url(#leadGold)"/>
    </svg>
    <div class="brand">
      <span class="brand__dot"></span>
      <p class="brand__name">Bright Meadow<br>Institute</p>
    </div>
    <h2 class="headline">
      Tantra Workshops
      <span class="headline__rule"></span>
      Store &amp; Vacation
    </h2>
    <a class="badge">LEARN<br>MORE</a>
  </section>

  <section class="banner rectangle" aria-label="300 by 250 banner">
    <div class="banner__photo photo--beach" role="img" aria-label="Photo of a couple sitting together on a tropical beach"></div>
    <svg class="banner__swoosh" viewBox="0 0 372 309" preserveAspectRatio="none" aria-hidden="true">
      <defs>
        <linearGradient id="rectGold" x1="0" y1="0" x2="1" y2="0">
          <stop offset="0" stop-color="#a8741a"/><stop offset="0.5" stop-color="#fbe38a"/><stop offset="1" stop-color="#e0b43a"/>
        </linearGradient>
      </defs>
      <path d="M0 0 H372 V126 C280 138 130 160 0 204 Z" fill="#050505"/>
      <path d="M0 204 C130 160 280 138 372 126 V137 C280 149 130 172 0 216 Z" fill="url(#rectGold)"/>
      <path d="M0 216 C130 172 280 149 372 137 V145 C280 157 130 180 0 224 Z" fill="#4a4a4a"/>
    </svg>
    <div class="brand">
      <span class="brand__dot"></span>
      <p class="brand__name">Bright Meadow<br>Institute</p>
    </div>
    <h2 class="headline">
      Tantra Workshops
      <span class="headline__rule"></span>
      Store &amp; Vacation
    </h2>
    <a class="badge">LEARN<br>MORE</a>
  </section>

</main>
</body>
</html>
```